Bright Forge Iron Client Handout

We need a cover sheet for our processes flyer that we will be handing out to our clients. Attached is a set of stairs that our company has erected, as well as our logos and a rough draft of what we are looking for. We would like the stairs in our image to be sharpened if at all possible, taken out from the background, and instead placed atop an image of a beautiful Arizona sunset/landscape. We would like the text to be editable and we would like to retain the rights to the product, as our language on this project is still being revised. We would also like the placement/positioning of our logos to be refined to look more modernized and professional.

Target Market(s)

Construction contractors, vendors and prospective builders.

Industry/Entity Type

Structural Steel

Requirements
Must have
• • clean up the background
• see if the stair image could be sharpened at all
• Put a beautiful AZ sunset behind it
• Refine location/layout of the BFI logo & header up top to make it a modernized, professional handout that we can give to clients
• NOTE: we may have a small amount of refining of the language used on the sub bullets so want to make sure we have the rights to the document to edit and revise it
Nice to have
• Please use our logo on this.
We would like a very Arizona-esque looking background. See link below for examples

https://www.examplefind.test/search?q=arizona+sunset&rlz=1X2YZAB_enUS100US100&sxsrf=QWeRt02abCDefGHijKLmnOPqrST5Uv:1500000000000&source=lnms&tbm=isch&sa=X&ved=3bcDEfghIjKlmNoPqRsTuVwXyZ0Q_BcDeFgHiJkLmNoPqRs&biw=1920&bih=969

```html
<!DOCTYPE html>
<html lang="en">
<head>
<meta charset="utf-8">
<title>Steel-Solid Stairway to Success — Cover Options</title>
<link rel="stylesheet" href="https://fonts.googleapis.com/css2?family=Merriweather:wght@400;700&family=Kanit:wght@600;700&display=swap">
<style>
  :root {
    --board: #a9a9a9;
    --label: #ffffff;
    --ink: #ffffff;
    --headline: #f3e6da;
    --footer: #ffffff;
    --brand: #2b2b2b;
    --sky-top: #4e3558;
    --sky-violet: #7b4868;
    --sky-rose: #b84e4e;
    --sky-orange: #e37c38;
    --sky-ember: #c0461f;
    --ground-dark: #2c1210;
    --ground-black: #080505;
  }
  * { box-sizing: border-box; margin: 0; padding: 0; }
  html, body { width: 1200px; height: 960px; overflow: hidden; }
  body { background: var(--board); position: relative; font-family: "Merriweather", serif; }

  .option-label {
    position: absolute; top: 76px; width: 300px; text-align: center;
    font-family: "Merriweather", serif; font-weight: 700; font-size: 24px;
    letter-spacing: 1px; color: var(--label);
  }
  .option-label--one { left: 154px; }
  .option-label--two { left: 722px; }

  .flyer {
    position: absolute; overflow: hidden;
    box-shadow: 12px 14px 18px rgba(0,0,0,0.35);
  }
  .flyer--one { left: 46px; top: 132px; width: 516px; height: 730px; }
  .flyer--two { left: 626px; top: 134px; width: 514px; height: 728px; background: var(--footer); }

  .sunset-scene {
    position: absolute; left: 0; top: 0; width: 100%; height: 100%;
    background: linear-gradient(180deg,
      var(--sky-top) 0%, var(--sky-violet) 18%, var(--sky-rose) 36%,
      var(--sky-orange) 52%, var(--sky-ember) 64%, var(--ground-dark) 78%,
      var(--ground-black) 92%);
  }
  .flyer--two .sunset-scene { height: 677px; }

  .brand {
    position: absolute; display: flex; align-items: center; gap: 6px;
    font-family: "Merriweather", serif; font-weight: 700; font-size: 14px; color: var(--ink);
  }
  .brand__mark { width: 14px; height: 14px; background: currentColor; }
  .flyer--one .brand { left: 360px; top: 26px; }
  .brand--footer {
    left: 0; right: 0; top: 677px; height: 51px; justify-content: center;
    color: var(--brand); font-size: 15px;
  }

  .title {
    position: absolute; left: 0; width: 100%; text-align: center;
    font-family: "Kanit", sans-serif; font-weight: 700; font-size: 40px; line-height: 1;
    letter-spacing: 3px; color: var(--headline);
  }
  .flyer--one .title { top: 76px; }
  .flyer--two .title { top: 35px; }

  .subtitle {
    position: absolute; left: 0; width: 100%; text-align: center;
    font-family: "Kanit", sans-serif; font-weight: 600; font-size: 21px;
    letter-spacing: 1px; color: var(--ink);
  }
  .flyer--one .subtitle { top: 121px; }
  .flyer--two .subtitle { top: 80px; }

  .step {
    position: absolute; width: 160px; transform: translateX(-50%);
    text-align: center; color: var(--ink);
  }
  .step__icon { display: block; margin: 0 auto 4px; width: 28px; height: 28px; }
  .step__icon path, .step__icon circle, .step__icon rect, .step__icon line, .step__icon polyline {
    fill: none; stroke: var(--ink); stroke-width: 1.4; stroke-linecap: round; stroke-linejoin: round;
  }
  .step__name { font-weight: 700; font-size: 12px; letter-spacing: 0.4px; line-height: 1.3; }
  .step__points { list-style: none; font-size: 10px; line-height: 1.3; }
</style>
</head>
<body>

<div class="option-label option-label--one">OPTION 1</div>
<div class="option-label option-label--two">OPTION 2</div>

<!-- Option 1 -->
<section class="flyer flyer--one">
  <div class="sunset-scene" role="img" aria-label="Steel switchback stairway silhouetted against an Arizona desert sunset with saguaro cacti"></div>
  <div class="brand"><span class="brand__mark"></span>Bright Forge Iron</div>
  <h1 class="title">STEEL-SOLID</h1>
  <h2 class="subtitle">STAIRWAY TO SUCCESS</h2>

  <div class="step" style="left:103px; top:188px;">
    <svg class="step__icon" viewBox="0 0 28 28"><rect x="5" y="3" width="14" height="20"/><line x1="8" y1="9" x2="15" y2="9"/><line x1="8" y1="13" x2="13" y2="13"/><line x1="8" y1="17" x2="12" y2="17"/><path d="M14 20 L23 8 L25 10 L16 22 L13 23 Z"/></svg>
    <div class="step__name">EVALUATE</div>
    <ul class="step__points"><li>• Post Project Assessment</li><li>• Client Satisfaction Score</li></ul>
  </div>
  <div class="step" style="left:428px; top:242px;">
    <svg class="step__icon" viewBox="0 0 28 28"><rect x="8" y="3" width="12" height="13"/><polyline points="12,3 12,10 14,8 16,10 16,3"/><path d="M3 19 L9 17 L15 19 L22 17 Q25 17 24 20 L16 24 L9 23 L3 24"/></svg>
    <div class="step__name">DELIVER</div>
    <ul class="step__points"><li>• Safely erect steel</li><li>• Blink and We Are Done</li></ul>
  </div>
  <div class="step" style="left:96px; top:308px;">
    <svg class="step__icon" viewBox="0 0 28 28"><path d="M5 3 H16 L20 7 V14 M5 3 V24 H14"/><line x1="8" y1="9" x2="15" y2="9"/><line x1="8" y1="13" x2="14" y2="13"/><circle cx="20" cy="20" r="4"/><circle cx="20" cy="20" r="1.5"/></svg>
    <div class="step__name">IMPLEMENT</div>
    <ul class="step__points"><li>• Contact During Fabrication (75% Completed Before We Shop Up)</li><li>• 3D Models Provided</li></ul>
  </div>
  <div class="step" style="left:428px; top:378px;">
    <svg class="step__icon" viewBox="0 0 28 28"><rect x="3" y="3" width="22" height="16"/><polyline points="7,15 11,10 14,13 19,7"/><line x1="14" y1="19" x2="9" y2="25"/><line x1="14" y1="19" x2="19" y2="25"/></svg>
    <div class="step__name">STRATEGIZE</div>
    <ul class="step__points"><li>• Steel-Solid Expectations Meeting</li><li>• Smarter, Faster, Better (Coordinate to Maximize Prefabrication)</li></ul>
  </div>
  <div class="step" style="left:98px; top:464px;">
    <svg class="step__icon" viewBox="0 0 28 28"><path d="M2 10 L7 8 L12 11 L17 8 L26 10 M4 12 L10 19 Q12 21 14 19 L20 13 M7 15 L11 19 M10 13 L15 18"/></svg>
    <div class="step__name">COLLABORATE</div>
    <ul class="step__points"><li>• Pre-Construction Value Engineering</li><li>• Budgeting Assistance</li></ul>
  </div>
  <div class="step" style="left:394px; top:542px;">
    <svg class="step__icon" viewBox="0 0 28 28"><circle cx="11" cy="11" r="7"/><path d="M8 9 Q10 6 13 7"/><line x1="16" y1="16" x2="24" y2="24"/></svg>
    <div class="step__name">DISCOVER</div>
    <ul class="step__points"><li>• Share our Steel Expertise (Best Practices)</li><li>• Identify Best Value Opportunities (What's Best for the Project)</li></ul>
  </div>
  <div class="step" style="left:181px; top:590px;">
    <svg class="step__icon" viewBox="0 0 28 28"><circle cx="9" cy="10" r="3.5"/><circle cx="19" cy="10" r="3.5"/><path d="M3 22 Q3 15 9 15 Q15 15 15 22 Z M13 22 Q13 15 19 15 Q25 15 25 22 Z"/></svg>
    <div class="step__name">STEEL-SOLID<br>RELATIONSHIPS</div>
    <ul class="step__points"><li>• Prior Success Foundation</li><li>• Zippered Relationships</li></ul>
  </div>
</section>

<!-- Option 2 -->
<section class="flyer flyer--two">
  <div class="sunset-scene" role="img" aria-label="Steel switchback stairway silhouetted against an Arizona desert sunset with saguaro cacti"></div>
  <h1 class="title">STEEL-SOLID</h1>
  <h2 class="subtitle">STAIRWAY TO SUCCESS</h2>

  <div class="step" style="left:102px; top:146px;">
    <svg class="step__icon" viewBox="0 0 28 28"><rect x="5" y="3" width="14" height="20"/><line x1="8" y1="9" x2="15" y2="9"/><line x1="8" y1="13" x2="13" y2="13"/><line x1="8" y1="17" x2="12" y2="17"/><path d="M14 20 L23 8 L25 10 L16 22 L13 23 Z"/></svg>
    <div class="step__name">EVALUATE</div>
    <ul class="step__points"><li>• Post Project Assessment</li><li>• Client Satisfaction Score</li></ul>
  </div>
  <div class="step" style="left:427px; top:199px;">
    <svg class="step__icon" viewBox="0 0 28 28"><rect x="8" y="3" width="12" height="13"/><polyline points="12,3 12,10 14,8 16,10 16,3"/><path d="M3 19 L9 17 L15 19 L22 17 Q25 17 24 20 L16 24 L9 23 L3 24"/></svg>
    <div class="step__name">DELIVER</div>
    <ul class="step__points"><li>• Safely erect steel</li><li>• Blink and We Are Done</li></ul>
  </div>
  <div class="step" style="left:86px; top:264px;">
    <svg class="step__icon" viewBox="0 0 28 28"><path d="M5 3 H16 L20 7 V14 M5 3 V24 H14"/><line x1="8" y1="9" x2="15" y2="9"/><line x1="8" y1="13" x2="14" y2="13"/><circle cx="20" cy="20" r="4"/><circle cx="20" cy="20" r="1.5"/></svg>
    <div class="step__name">IMPLEMENT</div>
    <ul class="step__points"><li>• Contact During Fabrication (75% Completed Before We Shop Up)</li><li>• 3D Models Provided</li></ul>
  </div>
  <div class="step" style="left:427px; top:334px;">
    <svg class="step__icon" viewBox="0 0 28 28"><rect x="3" y="3" width="22" height="16"/><polyline points="7,15 11,10 14,13 19,7"/><line x1="14" y1="19" x2="9" y2="25"/><line x1="14" y1="19" x2="19" y2="25"/></svg>
    <div class="step__name">STRATEGIZE</div>
    <ul class="step__points"><li>• Steel-Solid Expectations Meeting</li><li>• Smarter, Faster, Better (Coordinate to Maximize Prefabrication)</li></ul>
  </div>
  <div class="step" style="left:98px; top:422px;">
    <svg class="step__icon" viewBox="0 0 28 28"><path d="M2 10 L7 8 L12 11 L17 8 L26 10 M4 12 L10 19 Q12 21 14 19 L20 13 M7 15 L11 19 M10 13 L15 18"/></svg>
    <div class="step__name">COLLABORATE</div>
    <ul class="step__points"><li>• Pre-Construction Value Engineering</li><li>• Budgeting Assistance</li></ul>
  </div>
  <div class="step" style="left:392px; top:498px;">
    <svg class="step__icon" viewBox="0 0 28 28"><circle cx="11" cy="11" r="7"/><path d="M8 9 Q10 6 13 7"/><line x1="16" y1="16" x2="24" y2="24"/></svg>
    <div class="step__name">DISCOVER</div>
    <ul class="step__points"><li>• Share our Steel Expertise (Best Practices)</li><li>• Identify Best Value Opportunities (What's Best for the Project)</li></ul>
  </div>
  <div class="step" style="left:179px; top:546px;">
    <svg class="step__icon" viewBox="0 0 28 28"><circle cx="9" cy="10" r="3.5"/><circle cx="19" cy="10" r="3.5"/><path d="M3 22 Q3 15 9 15 Q15 15 15 22 Z M13 22 Q13 15 19 15 Q25 15 25 22 Z"/></svg>
    <div class="step__name">STEEL-SOLID<br>RELATIONSHIPS</div>
    <ul class="step__points"><li>• Prior Success Foundation</li><li>• Zippered Relationships</li></ul>
  </div>

  <div class="brand brand--footer"><span class="brand__mark"></span>Bright Forge Iron</div>
</section>

</body>
</html>
```